Letter Head Design - Finance industry

Design a letterhead to match the logo. Needs to be clean, simple and crisp. I'm open to suggestions. Will be using the logo that was submitted last with the W crossed over

Target Market(s)

Small medium businesses and government department's

Industry/Entity Type

Industry

Font styles to use
Sans Serif

Colors
cadf82
bcd85c
acd036
9bcb3c
e9e9e9
aaaaaa
000000
7f7f7f
b7b7b7

Requirements
Must have
• Need to display: Logo, Business address, ABN number, ASIC register number, contact phone, website, company email. Details are as per below:

Suite 4B Level 17
Marlowe Crest House
9 Tindall Lane
Sydney NSW 2000
Landline Ph: 02 5193 4620
Ph: 1300 4719 55
Email: enquiries@coinharbourco.com.au
W: www.coinharbourco.com.au

On the footer, the details below need to be specified:
ABN: 47 381 950 623
ASIC Registration Number: 31 749218605

Should not have
• No imagery or design that is not in line with the logo

```html
<!DOCTYPE html>
<html lang="en">
<head>
<meta charset="utf-8">
<title>Coin Harbour Co — Letterhead</title>
<link rel="stylesheet" href="https://fonts.googleapis.com/css2?family=PT+Sans:wght@400;700&display=swap">
<style>
  :root {
    --backdrop: #23262b;
    --paper: #ffffff;
    --brand-green: #a9cf3b;
    --mark-green: #acd036;
    --ink: #000000;
    --footer-ink: #4f5a2a;
    --footer-ink-strong: #1f2410;
  }
  * { box-sizing: border-box; margin: 0; padding: 0; }
  html, body {
    width: 1200px;
    height: 1000px;
    overflow: hidden;
    background: var(--backdrop);
    font-family: "PT Sans", sans-serif;
  }
  .letterhead {
    position: absolute;
    left: 267px;
    top: 30px;
    width: 666px;
    height: 940px;
    background: var(--paper);
    display: flex;
    flex-direction: column;
  }
  .letterhead__header {
    display: flex;
    align-items: center;
    gap: 14px;
    padding: 34px 0 0 34px;
  }
  .brand-dot {
    width: 52px;
    height: 52px;
    border-radius: 50%;
    background: var(--mark-green);
    flex: none;
  }
  .brand-name {
    font-size: 33px;
    font-weight: 400;
    color: var(--ink);
    line-height: 1;
  }
  .letterhead__body { flex: 1; }
  .letterhead__footer {
    height: 108px;
    background: var(--brand-green);
    text-align: center;
    padding-top: 17px;
    color: var(--footer-ink);
  }
  .footer-contacts {
    font-size: 9.5px;
    letter-spacing: 0.1px;
  }
  .footer-contacts .label { font-weight: 700; }
  .footer-contacts .sep { padding: 0 4px; }
  .footer-contacts .gap { padding-left: 10px; }
  .footer-web {
    margin-top: 6px;
    font-size: 13px;
    font-weight: 700;
    color: var(--footer-ink-strong);
  }
  .footer-registration {
    margin-top: 8px;
    font-size: 7.5px;
  }
  .footer-registration .label { font-weight: 700; }
  .footer-registration .item + .item { margin-left: 22px; }
</style>
</head>
<body>
  <main class="letterhead">
    <header class="letterhead__header">
      <span class="brand-dot" aria-hidden="true"></span>
      <span class="brand-name">Coin Harbour Co</span>
    </header>
    <section class="letterhead__body"></section>
    <footer class="letterhead__footer">
      <p class="footer-contacts">
        Suite 4B Level 17, Marlowe Crest House, 9 Tindall Lane, Sydney NSW 2000.
        <span class="gap"><span class="label">T:</span> 02 5193 4620</span>
        <span class="sep">|</span><span class="label">Ph:</span> 1300 4719 55
        <span class="sep">|</span><span class="label">E:</span> enquiries@coinharbourco.com.au
      </p>
      <p class="footer-web">www.coinharbourco.com.au</p>
      <p class="footer-registration">
        <span class="item"><span class="label">ABN:</span> 47 381 950 623</span>
        <span class="item"><span class="label">ASIC Registration Number:</span> 31 749218605</span>
      </p>
    </footer>
  </main>
</body>
</html>
```